Business Card Design Project

I need a business card designed that is clean, simple and elegant.
I am a fashion and advertising photographer based in Cape Town and Durban South Africa.
check out my website: www.brennowalsh.co.za for ideas
Updates
Hi all,
Thanks for your submissions so far!
Please note:
I want no more than than black, white and/or grey to be used.
I don't want any photos used.
I would like the card to be double sided.
I would like to continue the design similar to the past ones Ive used.
I hope this helps, please send me further questions should you have any.
many thanks!
Brenno
Hi,
Please have a look at the jpg I loaded(called inspiration) which is the direction or inspiration I am aiming at.
Also PLEASE remember NO PHOTOS to be included on the card
many thanks!!
Target Market(s)
You can look at my site to get a better understanding of the audience:
www.brennowalsh.co.za
Industry/Entity Type
Advertising
Requirements
Must have
- Clean design which can also be used for a watermark on photographs
perhaps black background with white text/grey
company called: Brenno Walsh Photography
Nice to have
- below I have added logos that I have used in the past.
Should not have
- pictures of cameras
tacky elements

```html
<!DOCTYPE html>
<html lang="en">
<head>
<meta charset="utf-8">
<title>Brenno Walsh Photography – Business Card</title>
<link rel="stylesheet" href="https://fonts.googleapis.com/css2?family=Electrolize&display=swap">
<style>
  :root {
    --page: #ffffff;
    --card: #000000;
    --name: #ffffff;
    --tagline: #9a9a9a;
    --mark-dark: #2a2a2a;
    --mark-text: #8c8c8c;
  }
  html, body {
    margin: 0;
    padding: 0;
    background: var(--page);
    overflow: hidden;
  }
  .canvas {
    position: relative;
    width: 1200px;
    height: 667px;
    overflow: hidden;
    background: var(--page);
    font-family: "Electrolize", sans-serif;
  }
  .card {
    position: absolute;
    left: 27px;
    top: 34px;
    width: 1136px;
    height: 598px;
    border-radius: 46px;
    background: var(--card);
    overflow: hidden;
  }
  .card__name {
    margin: 0;
    position: absolute;
    left: 368px;
    top: 228px;
    transform: translateX(-50%);
    font-size: 56px;
    font-weight: 400;
    letter-spacing: 0;
    color: var(--name);
    line-height: 1;
    white-space: nowrap;
  }
  .card__tagline {
    margin: 0;
    position: absolute;
    left: 368px;
    top: 318px;
    transform: translateX(-50%);
    font-size: 42px;
    color: var(--tagline);
    line-height: 1;
    white-space: nowrap;
  }
  .brand-mark {
    position: absolute;
    left: 760px;
    top: 150px;
    width: 300px;
    display: flex;
    flex-direction: column;
    align-items: center;
  }
  .brand-mark__dot {
    width: 200px;
    height: 200px;
    border-radius: 50%;
    background: var(--mark-dark);
  }
  .brand-mark__name {
    margin: 28px 0 0;
    font-size: 26px;
    font-weight: 400;
    color: var(--mark-text);
    letter-spacing: 1px;
    white-space: nowrap;
  }
</style>
</head>
<body>
  <div class="canvas">
    <section class="card">
      <h1 class="card__name">BRENNO WALSH</h1>
      <p class="card__tagline">........Photography........</p>

      <div class="brand-mark">
        <div class="brand-mark__dot"></div>
        <p class="brand-mark__name">BRENNO WALSH</p>
      </div>
    </section>
  </div>
</body>
</html>
```